Package for Utensil Kit

we want to have a new design for our utensil kit, its a paper bag with both sides like files below. our website is www.peckbox.com and please use #FF6C0E as the main color and feel free to unleash your creativity.
the deadcut of the package is 14x26cm.pdf also showed the size.
in the front we want to show our band
in the back we need info list here:
1. www.peckbox.com and QR code
2.our locations (Now four) and phone number
3.other information needed

```html
<!DOCTYPE html>
<html lang="en">
<head>
<meta charset="utf-8">
<title>Peckbox Utensil Kit – Front and Back</title>
<link rel="stylesheet" href="https://fonts.googleapis.com/css2?family=Archivo:wght@300;400;700;800&display=swap">
<style>
  :root {
    --orange-main: #F26C27;
    --orange-warm: #EC8A2C;
    --cream: #FCE6C6;
    --white: #FFFFFF;
    --ink: #111111;
  }
  * { box-sizing: border-box; margin: 0; padding: 0; }
  html, body {
    width: 1200px; height: 1169px; overflow: hidden;
    background: var(--white);
    font-family: "Archivo", Arial, sans-serif;
  }
  .canvas { position: relative; width: 1200px; height: 1169px; }

  .panel { position: absolute; top: 73px; width: 477px; height: 1026px; overflow: hidden; }
  .panel-front { left: 119px; background: var(--orange-main); }
  .panel-back { left: 632px; }

  /* Front */
  .front-artwork {
    position: absolute; inset: 0;
    background:
      radial-gradient(ellipse 60% 35% at 80% 15%, var(--cream) 0%, rgba(252,230,198,0) 70%),
      radial-gradient(ellipse 45% 30% at 10% 30%, rgba(252,230,198,.85) 0%, rgba(252,230,198,0) 70%),
      radial-gradient(ellipse 60% 30% at 20% 70%, rgba(252,230,198,.7) 0%, rgba(252,230,198,0) 70%),
      linear-gradient(180deg, var(--orange-warm) 0%, var(--orange-main) 45%, var(--orange-main) 80%, var(--orange-warm) 100%);
  }
  .brand-badge {
    position: absolute; left: 24px; top: 247px;
    width: 424px; height: 424px; border-radius: 50%;
    background: var(--orange-main);
    border: 11px solid var(--white);
    display: flex; align-items: center; justify-content: center;
  }
  .brand-name {
    color: var(--white); font-weight: 800; font-size: 74px; letter-spacing: -2px;
  }
  .front-tagline {
    position: absolute; left: 0; right: 0; top: 820px;
    text-align: center; color: var(--white);
    font-weight: 800; font-size: 44px; line-height: 46px; letter-spacing: -1.5px;
  }

  /* Back */
  .back-shapes { position: absolute; inset: 0; width: 100%; height: 100%; }
  .back-website {
    position: absolute; left: 34px; top: 94px;
    color: var(--cream); font-weight: 800; font-size: 23px; letter-spacing: -0.5px;
  }
  .qr-frame {
    position: absolute; left: 318px; top: 57px; width: 125px; height: 125px;
    background: var(--white); padding: 5px;
  }
  .qr-frame span { display: block; width: 100%; height: 100%; border: 4px solid var(--ink); }

  .locations { position: absolute; left: 39px; top: 282px; color: var(--cream); }
  .locations-title { font-weight: 400; font-size: 25px; letter-spacing: -1px; margin-bottom: 16px; }
  .location { margin-bottom: 21px; }
  .location-name { font-weight: 700; font-size: 21px; letter-spacing: -0.5px; line-height: 24px; }
  .location-address { font-weight: 300; font-size: 21px; line-height: 19px; letter-spacing: -0.3px; font-style: normal; }

  .sign-off {
    position: absolute; left: 32px; top: 825px;
    color: var(--orange-main); font-weight: 800; font-size: 32px; line-height: 34px; letter-spacing: -1px;
  }
</style>
</head>
<body>
<main class="canvas">

  <section class="panel panel-front" aria-label="Front of bag">
    <div class="front-artwork" role="img" aria-label="Illustration of roosters and hens with dotted and spiral patterns in orange and cream"></div>
    <div class="brand-badge"><span class="brand-name">Peckbox</span></div>
    <h1 class="front-tagline">Authentic<br>Hainan Chicken</h1>
  </section>

  <section class="panel panel-back" aria-label="Back of bag">
    <svg class="back-shapes" viewBox="0 0 779 1676" preserveAspectRatio="none" aria-hidden="true">
      <rect width="779" height="1676" fill="var(--orange-warm)"/>
      <path d="M0,312 C150,290 300,300 450,370 C560,420 660,470 779,400 L779,520 L0,520 Z" fill="var(--cream)"/>
      <path d="M0,406 C100,330 250,340 400,400 C520,450 640,500 779,458 L779,1676 L0,1676 Z" fill="var(--orange-main)"/>
      <path d="M0,1295 C150,1250 330,1260 430,1360 C540,1460 580,1570 530,1676 L0,1676 Z" fill="var(--cream)"/>
    </svg>

    <p class="back-website">www.peckbox.com</p>
    <div class="qr-frame" aria-label="QR code space"><span></span></div>

    <div class="locations">
      <h2 class="locations-title">OUR LOCATIONS</h2>
      <div class="location">
        <h3 class="location-name">Location 1</h3>
        <address class="location-address">1235 Street,<br>Hainan CA 92005</address>
      </div>
      <div class="location">
        <h3 class="location-name">Location 2</h3>
        <address class="location-address">1235 Street,<br>Hainan CA 92005</address>
      </div>
      <div class="location">
        <h3 class="location-name">Location 3</h3>
        <address class="location-address">1235 Street,<br>Hainan CA 92005</address>
      </div>
      <div class="location">
        <h3 class="location-name">Location 4</h3>
        <address class="location-address">1235 Street,<br>Hainan CA 92005</address>
      </div>
    </div>

    <p class="sign-off">Enjoy!<br>#Peckbox</p>
  </section>

</main>
</body>
</html>
```